Business card for biotech sales agent

I need a logo and business card designed for my company Belunor. We work in partnership with Kestrel Group. Kestrel have developed advanced biotech. Their hand sanitiser is alcohol free and works for 24 hours on skin, even with regular hand washing. The surface sanitiser works for up to 30 days on surfaces and fabrics. Its food-safe, it's non-toxic, safe for animals and humans. The products have a very wide variety of applications: everything from agri-business, hotels, hospitality, schools, child and baby care, transport, meat processing etc.<br/>I would like my design to use blues or green-blues and communicate a bit of nano-tech but also trust and safety.<br/>I would also use the Kestrel logo on my card next to 'sales & distribution agent'

Target Market(s)

B2B, selling to FMCG and large companies such as airlines

Industry/Entity Type

Biotechnology

Contact Information for Business Card

Helen Pritch
Director

Phone: +64 22 519 3064
Email: helen@belunor.co
www.belunor.co
7 Tamsin St, Newmarket, Auckland, New Zealand 1023

Font styles to use
Sans Serif

Colors
3276b5
33b8a4
34a7d8
3176b5
ffffff

Requirements
Must have
• Not be too busy, clean space is good
• A logo styling to the word Belunor
Nice to have
• A little bit of a bio-tech image as a screen perhaps

```html
<!DOCTYPE html>
<html lang="en">
<head>
<meta charset="utf-8">
<title>Belunor Business Card</title>
<link rel="stylesheet" href="https://fonts.googleapis.com/css2?family=Montserrat:wght@500;600;700;800&display=swap">
<style>
  :root {
    --brand-blue: #3276b5;
    --brand-sky: #34a7d8;
    --ink: #1b1f2a;
    --paper: #ffffff;
    --backdrop: #eef1f5;
  }
  * { margin: 0; padding: 0; box-sizing: border-box; }
  html, body { width: 1200px; height: 1000px; overflow: hidden; }
  body {
    background: var(--backdrop);
    font-family: "Montserrat", Arial, sans-serif;
    position: relative;
  }
  .card {
    position: absolute;
    left: 228px;
    width: 745px;
    height: 400px;
    overflow: hidden;
    box-shadow: 0 6px 24px rgba(20, 40, 70, 0.18);
  }
  .card--front { top: 70px; }
  .card--back { top: 530px; background: var(--paper); }

  .front-texture {
    position: absolute;
    inset: 0;
    background: linear-gradient(115deg, var(--brand-blue) 0%, #3386c4 55%, var(--brand-sky) 100%);
  }
  .front-content { position: absolute; left: 29px; top: 224px; color: var(--paper); }
  .wordmark { font-weight: 600; letter-spacing: 2px; line-height: 1; }
  .front-content .wordmark { font-size: 54px; }
  .person-name { font-size: 27px; font-weight: 600; letter-spacing: 0.5px; margin-top: 24px; line-height: 1; }
  .person-role { font-size: 12px; font-weight: 500; letter-spacing: 0.3px; margin-top: 8px; }

  .back-content { position: absolute; inset: 0; }
  .back-content .wordmark {
    position: absolute; left: 0; right: 0; top: 28px;
    text-align: center; font-size: 54px; color: var(--brand-blue);
  }
  .back-identity { position: absolute; left: 36px; top: 133px; }
  .back-identity .person-name { color: var(--brand-blue); margin-top: 0; }
  .back-identity .person-role { color: var(--ink); margin-top: 11px; }

  .contact {
    position: absolute;
    display: flex; align-items: center; gap: 12px;
    font-size: 15px; font-weight: 700; color: var(--ink);
  }
  .contact svg { width: 28px; height: 28px; flex: none; }
  .contact--phone { left: 39px; top: 212px; }
  .contact--email { left: 282px; top: 212px; }
  .contact--web { left: 508px; top: 212px; }
  .contact--address { left: 39px; top: 254px; }

  .partner { position: absolute; left: 38px; top: 316px; }
  .partner-label { font-size: 18px; font-weight: 600; color: var(--brand-blue); }
  .partner-name { font-size: 20px; font-weight: 800; color: var(--ink); letter-spacing: 1px; margin-top: 6px; }
</style>
</head>
<body>
  <section class="card card--front">
    <div class="front-texture" role="img" aria-label="Blue hexagonal nano-tech pattern background"></div>
    <div class="front-content">
      <div class="wordmark">BELUNOR</div>
      <div class="person-name">HELEN PRITCH</div>
      <div class="person-role">DIRECTOR</div>
    </div>
  </section>

  <section class="card card--back">
    <div class="back-content">
      <div class="wordmark">BELUNOR</div>
      <div class="back-identity">
        <div class="person-name">HELEN PRITCH</div>
        <div class="person-role">DIRECTOR</div>
      </div>

      <div class="contact contact--phone">
        <svg viewBox="0 0 28 28" aria-hidden="true"><circle cx="14" cy="14" r="14" fill="#3276b5"/><path d="M10.5 8.5l2 2.6-1.3 1.5c.8 1.7 2.1 3 3.8 3.8l1.5-1.3 2.6 2-1 1.9c-4.7-.4-8.6-4.3-9-9z" fill="#fff"/></svg>
        <span>+64 22 519 3064</span>
      </div>
      <div class="contact contact--email">
        <svg viewBox="0 0 28 28" aria-hidden="true"><circle cx="14" cy="14" r="14" fill="#3276b5"/><rect x="8" y="9.5" width="12" height="9" rx="1" fill="#fff"/><path d="M8.5 10l5.5 4.5 5.5-4.5" stroke="#3276b5" stroke-width="1.2" fill="none"/></svg>
        <span>helen@belunor.co</span>
      </div>
      <div class="contact contact--web">
        <svg viewBox="0 0 28 28" aria-hidden="true"><circle cx="14" cy="14" r="14" fill="#3276b5"/><g stroke="#fff" stroke-width="1.2" fill="none"><circle cx="14" cy="14" r="6"/><ellipse cx="14" cy="14" rx="2.6" ry="6"/><path d="M8 14h12M9 11h10M9 17h10"/></g></svg>
        <span>www.belunor.co</span>
      </div>
      <div class="contact contact--address">
        <svg viewBox="0 0 28 28" aria-hidden="true"><circle cx="14" cy="14" r="14" fill="#3276b5"/><path d="M14 7.5a4.5 4.5 0 0 0-4.5 4.5c0 3.4 4.5 8.5 4.5 8.5s4.5-5.1 4.5-8.5A4.5 4.5 0 0 0 14 7.5z" fill="#fff"/><circle cx="14" cy="12" r="1.7" fill="#3276b5"/></svg>
        <span>7 Tamsin St, Newmarket, Auckland, New Zealand 1023</span>
      </div>

      <div class="partner">
        <div class="partner-label">Sales &amp; Distribution Agent</div>
        <div class="partner-name">KESTREL</div>
      </div>
    </div>
  </section>
</body>
</html>
```